Larkwood Bend Campground Billboard

We need an eye-catching, traffic-stopping design for a 15 ft x 10 ft billboard that will be located near the turn-off to our RV park in Colorado. Our park is located on the banks of the Rio Grande River and we want to emphasize that we have shady spots on the river. This is a link to our website www.larkwoodbendcampground.com and it will give you an idea about our park and what we have to offer. The billboard will be double-sided and face both directions of a busy highway. The park and the river is not visible from the highway, so we want to attract attention.

Target Market(s)

RV travelers on US Hwy 160 in South Fork, Colorado

Font styles to use
Sans Serif

Colors

Designer to choose colors to be used in the design.

Requirements
Must have
• Simple, eye-catching message.
Nice to have
• Incorporate our logo and give directions.
Should not have
• Too much information that can't be read while speeding down a busy highway.

```html
<!DOCTYPE html>
<html lang="en">
<head>
<meta charset="utf-8">
<title>Larkwood Bend Campground Billboard</title>
<link href="https://fonts.googleapis.com/css2?family=Montserrat:wght@600;800&display=swap" rel="stylesheet">
<style>
  :root {
    --page: #e8ebe4;
    --board-green: #8ba167;
    --scene-light: #a3b47f;
    --scene-dark: #6f8a52;
    --badge-dark: #1d3118;
    --icon-green: #b8d97c;
    --band: #8c7b68;
    --white: #ffffff;
    --outline: #1a2614;
  }
  * { box-sizing: border-box; margin: 0; padding: 0; }
  html, body { width: 1200px; height: 1000px; overflow: hidden; background: var(--page); }
  .billboard {
    position: absolute; left: 30px; top: 90px; width: 1140px; height: 820px;
    background: var(--board-green); overflow: hidden;
    font-family: "Montserrat", sans-serif;
  }
  .scenery {
    position: absolute; inset: 0 0 97px 0;
    background: linear-gradient(180deg, var(--scene-light) 0%, var(--scene-dark) 45%, var(--board-green) 70%, var(--scene-light) 100%);
    opacity: .85;
  }
  .brand {
    position: absolute; left: 0; right: 0; top: 150px;
    text-align: center; color: var(--white);
    font-weight: 800; font-size: 64px; line-height: 1.1; text-transform: uppercase; letter-spacing: 1px;
  }
  .amenities {
    position: absolute; top: 460px; left: 0; right: 0; height: 220px;
  }
  .amenity { position: absolute; width: 240px; margin-left: -120px; text-align: center; }
  .amenity svg { display: block; margin: 0 auto; }
  .amenity-label {
    margin-top: 18px; color: var(--white); font-weight: 800; font-size: 31px; line-height: 1.05;
    text-transform: uppercase;
    text-shadow: 2px 2px 0 var(--outline), -2px -2px 0 var(--outline), 2px -2px 0 var(--outline), -2px 2px 0 var(--outline);
  }
  .contact-band {
    position: absolute; left: 0; right: 0; bottom: 0; height: 97px;
    background: var(--band); display: flex; align-items: center; justify-content: center; color: var(--white);
  }
  .phone { font-weight: 600; font-size: 47px; padding-right: 36px; }
  .divider { width: 2px; height: 62px; background: var(--white); }
  .website { font-weight: 600; font-size: 30px; padding-left: 36px; }
</style>
</head>
<body>
  <main class="billboard">
    <div class="scenery" role="img" aria-label="Green-tinted photo of a forested mountain lake"></div>

    <h1 class="brand">Larkwood Bend<br>Campground</h1>

    <section class="amenities">
      <div class="amenity" style="left:228px">
        <svg width="140" height="140" viewBox="0 0 140 140" aria-hidden="true">
          <circle cx="70" cy="70" r="67" fill="var(--badge-dark)" stroke="var(--outline)" stroke-width="3"/>
          <rect x="28" y="48" width="80" height="40" rx="6" fill="var(--icon-green)"/>
          <path d="M108 60h8l6 14v14h-14z" fill="var(--icon-green)"/>
          <rect x="38" y="56" width="16" height="12" fill="var(--badge-dark)"/>
          <rect x="62" y="56" width="16" height="12" fill="var(--badge-dark)"/>
          <circle cx="48" cy="92" r="8" fill="var(--icon-green)" stroke="var(--badge-dark)" stroke-width="3"/>
          <circle cx="100" cy="92" r="8" fill="var(--icon-green)" stroke="var(--badge-dark)" stroke-width="3"/>
        </svg>
        <p class="amenity-label">RV Spaces</p>
      </div>
      <div class="amenity" style="left:488px">
        <svg width="140" height="140" viewBox="0 0 140 140" aria-hidden="true">
          <circle cx="70" cy="70" r="67" fill="var(--badge-dark)" stroke="var(--outline)" stroke-width="3"/>
          <circle cx="70" cy="70" r="50" fill="var(--icon-green)"/>
          <path d="M82 22c-20 10 6 22-10 34s-18 18 0 28-16 24-16 34" fill="none" stroke="var(--badge-dark)" stroke-width="7" stroke-linecap="round"/>
        </svg>
        <p class="amenity-label">Riverfront<br>Spaces</p>
      </div>
      <div class="amenity" style="left:742px">
        <svg width="140" height="140" viewBox="0 0 140 140" aria-hidden="true">
          <circle cx="70" cy="70" r="67" fill="var(--badge-dark)" stroke="var(--outline)" stroke-width="3"/>
          <path d="M70 34L28 96h84z" fill="var(--icon-green)"/>
          <path d="M70 56L58 96h24z" fill="var(--badge-dark)"/>
        </svg>
        <p class="amenity-label">Tent Sites</p>
      </div>
      <div class="amenity" style="left:944px">
        <svg width="140" height="140" viewBox="0 0 140 140" role="img" aria-label="Fishing icon">
          <circle cx="70" cy="70" r="67" fill="var(--badge-dark)" stroke="var(--outline)" stroke-width="3"/>
          <circle cx="70" cy="70" r="36" fill="var(--icon-green)"/>
        </svg>
        <p class="amenity-label">Fishing</p>
      </div>
    </section>

    <footer class="contact-band">
      <span class="phone">800.555.0143</span>
      <span class="divider"></span>
      <span class="website">www.larkwoodbendcampground.com</span>
    </footer>
  </main>
</body>
</html>
```